VORELLI Industrial Maintenance

I offer repair and maintenance services of industrial mechanics in Quebec. I would like a creation that reflects confidence, competence, professionalism and dynamism. I like the orange color and the blue color.

Target Market(s)

Industries and Manufacturing companies using industrial machinery for the manufacture of their products.

Industry/Entity Type

Manufacturing

Contact Information for Business Card

VORELLI Maintenance Industrielle
Tél: (450)-318-5907
Courriel: vorelli.mnt@brastomail.com

Font styles to use
Sans Serif

Colors
f78f20
0455a3

Requirements
Must have
• My company name: VORELLI Maintenance Industrielle My phone: (450) -318-5907 My email: vorelli.mnt@brastomail.com
Nice to have
• Integrate a representative logo of the mechanics (gears, mechanical parts)

```html
<!DOCTYPE html>
<html lang="fr">
<head>
<meta charset="utf-8">
<title>VORELLI Maintenance Industrielle – Carte d'affaires</title>
<link rel="stylesheet" href="https://fonts.googleapis.com/css2?family=Poppins:wght@400;500;600;700&display=swap">
<style>
  :root {
    --orange: #f78f20;
    --orange-light: #fba544;
    --orange-glow: rgba(251, 170, 80, 0.55);
    --blue: #0455a3;
    --blue-soft: #2a6fb8;
    --white: #ffffff;
    --backdrop: #ececec;
  }
  * { margin: 0; padding: 0; box-sizing: border-box; }
  html, body {
    width: 1200px; height: 834px; overflow: hidden;
    background: var(--backdrop);
    font-family: "Poppins", sans-serif;
  }
  .business-card {
    position: absolute;
    left: 120px; top: 143px;
    width: 960px; height: 548px;
    background: radial-gradient(circle at 50% 38%, var(--orange-light) 0%, var(--orange) 55%);
    overflow: hidden;
    box-shadow: 0 10px 30px rgba(0,0,0,0.18);
  }
  .decor-area {
    position: absolute;
    right: 0; top: 120px;
    width: 360px; height: 220px;
    background: radial-gradient(ellipse at 70% 90%, var(--orange-glow) 0%, transparent 70%);
  }
  .contact-band {
    position: absolute;
    left: 0; right: 0; top: 340px; bottom: 0;
    background: var(--blue);
  }
  .band-decor-area {
    position: absolute;
    right: 0; bottom: 0;
    width: 120px; height: 90px;
    background: linear-gradient(135deg, var(--blue) 0%, var(--blue-soft) 100%);
  }
  .band-marker {
    position: absolute;
    left: 464px; top: 326px;
    width: 28px; height: 28px;
    background: var(--orange);
    transform: rotate(45deg);
  }
  .band-marker::after {
    content: "";
    position: absolute;
    left: 8px; top: 8px;
    width: 12px; height: 12px;
    background: var(--blue);
  }
  .brand {
    position: absolute;
    left: 0; right: 0; top: 110px;
    text-align: center;
    color: var(--white);
  }
  .brand-mark {
    display: block;
    width: 58px; height: 58px;
    margin: 0 auto 14px;
    border-radius: 50%;
    background: var(--blue);
  }
  .brand-name {
    font-weight: 700;
    font-size: 64px;
    line-height: 1;
    letter-spacing: 2px;
  }
  .brand-tagline {
    margin-top: 8px;
    font-weight: 500;
    font-size: 15px;
    letter-spacing: 2px;
  }
  .holder {
    position: absolute;
    left: 56px; top: 372px;
    color: var(--white);
  }
  .holder-name {
    font-weight: 600;
    font-size: 30px;
    letter-spacing: 2px;
  }
  .holder-role {
    font-weight: 400;
    font-size: 14px;
    letter-spacing: 1.5px;
  }
  .contact-list {
    position: absolute;
    left: 560px; top: 386px;
    list-style: none;
    color: var(--white);
    font-size: 18px;
    line-height: 34px;
  }
  .contact-list li { display: flex; align-items: center; gap: 12px; }
  .contact-list svg { width: 16px; height: 16px; fill: var(--white); flex: none; }
</style>
</head>
<body>
  <div class="business-card">
    <div class="decor-area" role="img" aria-label="Zone de motif décoratif mécanique, teinte orange pâle"></div>
    <div class="contact-band"></div>
    <div class="band-decor-area" role="img" aria-label="Zone de motif décoratif mécanique, teinte bleue"></div>
    <div class="band-marker"></div>

    <div class="brand">
      <span class="brand-mark"></span>
      <div class="brand-name">VORELLI</div>
      <div class="brand-tagline">MAINTENANCE INDUSTRIELLE</div>
    </div>

    <div class="holder">
      <div class="holder-name">JULIEN MARCOTTE</div>
      <div class="holder-role">ÉLECTROMÉCANICIEN</div>
    </div>

    <ul class="contact-list">
      <li>
        <svg viewBox="0 0 24 24" aria-hidden="true"><path d="M6.6 10.8a15.1 15.1 0 0 0 6.6 6.6l2.2-2.2c.3-.3.7-.4 1-.2 1.1.4 2.3.6 3.6.6.6 0 1 .4 1 1V20c0 .6-.4 1-1 1C10.6 21 3 13.4 3 4c0-.6.4-1 1-1h3.5c.6 0 1 .4 1 1 0 1.3.2 2.5.6 3.6.1.3 0 .7-.2 1z"/></svg>
        (450)-318-5907
      </li>
      <li>
        <svg viewBox="0 0 24 24" aria-hidden="true"><path d="M2 5h20v14H2zm2 2v.5l8 5 8-5V7zm0 2.8V17h16V9.8l-8 5z"/></svg>
        vorelli.mnt@brastomail.com
      </li>
      <li>
        <svg viewBox="0 0 24 24" aria-hidden="true"><path d="M12 2a7 7 0 0 0-7 7c0 5.2 7 13 7 13s7-7.8 7-13a7 7 0 0 0-7-7zm0 9.5A2.5 2.5 0 1 1 12 6.5a2.5 2.5 0 0 1 0 5z"/></svg>
        Quebec, Canada
      </li>
    </ul>
  </div>
</body>
</html>
```